Brightwave Youth Academy is to provide global summer programs in the United States through which students from the US and China share experiences, intensive learning, and each other’s cultures. The program seeks to more fully prepare both the US and Chinese students for their college education and future careers in this interdependent world. Chinese students are individually paired with US Students where they will reside US students' home for the period of the program.

Current website: Brightwave Youth Academy

Need to support both English and Chinese with different font.
Updates

Project Deadline Extended
Reason: Because of Thanksgiving Holidays.

Dear Designers,

In order to generate the best design, I uploaded some photos from our global summer program. Please check:

http://brightwaveyouthacademy.org/photos/

Doreen

My company Logo just added to the project.

Sorry for the late update.

Project Deadline Extended
Reason: Due to Thanksgiving holiday, I don't have enough time to provide feedback to all the designers. Doreen

Project Deadline Extended
Reason: Holiday season. Need more time for designer and myself.

Target Market(s)

Grade K to 12 students and their parents to sign up the global summer program. Majority audience are from China.

Industry/Entity Type

College

Font styles to use
Sans Serif

Colors
3277b5

Requirements
Must have
• You may check my current website for the summer program content
www.brightwaveyouthacademy.org
Check these two clips to see what service we provided.
http://www.vidplexo.com/watch?v=9kR3mq41bTz&feature=vidplexo.be
https://www.vidplexo.com/watch?v=W7d2HN5p8oJ

Company Logo are included in the attachment.

Some photos from summer program: http://brightwaveyouthacademy.org/photos/
The website should show the students one to one relationship.
The website should show homestay part.

I want Photo Slider on each page to share the fun activities.

Each program will be provide a video clip as a summery.

The website should support font of both English and Chinese. I like to see both Chinese and English on the same page instead of switch back and forth. I can add Chinese part later if you leave the room.

Nice to have
• I have a lot of paired pictures. I am wondering if I can use collage of photos as the background.

The design should be playful and fun!

```html
<!DOCTYPE html>
<html lang="en">
<head>
<meta charset="utf-8">
<title>Brightwave Youth Academy</title>
<link href="https://fonts.googleapis.com/css2?family=Open+Sans:ital,wght@0,400;0,600;0,700;1,400&family=Noto+Sans+SC:wght@400;700&display=swap" rel="stylesheet">
<style>
:root{
  --blue:#0b6bbd;
  --blue-dark:#0a5aa0;
  --orange:#ff5a00;
  --ink:#222;
  --text:#444;
  --bar:#111;
  --footer:#2b2b2b;
  --footer-deep:#1a1a1a;
  --page:#e4e9f3;
}
*{box-sizing:border-box;margin:0;padding:0}
html,body{width:1200px;height:2341px;overflow:hidden}
body{position:relative;font-family:"Open Sans","Noto Sans SC",sans-serif;color:var(--text);
  background:linear-gradient(180deg,#eef1f7 0%,var(--page) 40%,#dfe5f1 100%)}
.abs{position:absolute}
.topbar{left:0;top:0;width:1200px;height:36px;background:var(--bar);color:#fff;font-size:12px}
.topbar ul{list-style:none;position:absolute;left:131px;top:11px;display:flex;gap:20px}
.topbar li::before{content:"• "}
.social{position:absolute;right:130px;top:8px;display:flex;gap:6px}
.social span{width:19px;height:19px;background:#3a7bc4;border-radius:2px}
.header{left:0;top:36px;width:1200px;height:128px;background:#fff}
.brand{position:absolute;left:145px;top:28px;display:flex;align-items:center;gap:10px}
.brand i{width:44px;height:44px;border-radius:50%;background:var(--blue)}
.brand b{font-size:22px;font-weight:700;color:var(--blue)}
.search{position:absolute;left:850px;top:51px;width:220px;height:28px;border:1px solid #bbb;background:#f6f6f6;font-size:11px;font-style:italic;color:#888;padding:6px 10px}
.search svg{position:absolute;right:8px;top:8px}
.nav{left:130px;top:164px;width:940px;height:47px;background:var(--blue);display:flex;align-items:center;font-size:12px;color:#fff;overflow:hidden}
.nav .active{flex:0 0 86px;background:var(--orange);line-height:47px;text-align:center;white-space:nowrap}
.nav .items{flex:1;display:flex;justify-content:space-evenly;white-space:nowrap}
.hero{left:130px;top:211px;width:940px;height:415px;background:linear-gradient(160deg,#5a6b7c 0%,#8a7a66 35%,#3f6b3a 60%,#a23b3b 85%,#6b5a4a 100%)}
.hero-caption{left:130px;top:301px;width:397px;height:198px;background:rgba(60,70,85,.72);color:#fff;padding:20px 15px}
.hero-caption h1{font-size:22px;font-weight:600;line-height:1}
.hero-caption h2{font-size:15px;font-weight:600;margin:4px 0 8px}
.hero-caption p{font-size:11px;font-weight:600;line-height:18px}
.btn-read{display:inline-block;margin-top:14px;background:var(--blue-dark);padding:9px 30px;font-size:14px;font-weight:600}
.dots{left:574px;top:609px;display:flex;gap:5px}
.dots span{width:8px;height:8px;border-radius:50%;background:var(--orange)}
.dots span:first-child{background:#fff}
.perk{width:240px}
.perk h3{font-size:16px;font-weight:700;color:var(--ink);margin-left:58px;margin-top:5px;white-space:nowrap}
.perk p{font-size:12px;line-height:18px;margin-left:58px;margin-top:10px;color:#555;white-space:nowrap}
.perk svg{position:absolute;left:0;top:0}
.sec-title{height:24px;display:flex;align-items:center;gap:8px;font-size:18px;color:var(--blue);white-space:nowrap}
.sec-title::after{content:"";flex:1;height:12px;background:repeating-linear-gradient(135deg,#bbb 0 1px,transparent 1px 4px)}
.feature{width:209px}
.feature .ph{width:209px;height:119px}
.feature p{font-size:11.5px;line-height:18px;margin-top:16px;color:#444;white-space:nowrap}
.btn{display:inline-block;background:var(--orange);color:#fff;border-radius:12px;font-size:12px;padding:3px 18px;margin-top:18px}
.videos p{font-size:11.5px;line-height:23px;color:#444}
.videos ul{list-style:none;margin-top:18px}
.videos li{font-size:11.5px;font-weight:700;color:#333;height:31px;display:flex;align-items:center;gap:16px}
.videos li.hot{color:var(--orange)}
.player{left:751px;top:1214px;width:319px;height:194px;background:linear-gradient(180deg,#8a6b5a 0%,#a08670 50%,#6a7785 100%)}
.player-bar{left:751px;top:1378px;width:319px;height:30px;background:#111}
.course{left:130px;top:1518px;width:304px;height:344px;background:var(--blue);border-radius:4px;color:#fff;padding:28px 24px}
.course h4{font-size:14px;font-weight:400;margin-bottom:14px}
.course .field{background:#fff;height:32px;border-radius:3px;font-size:11px;font-style:italic;color:#888;padding:9px 12px}
.course .btn{font-style:italic;font-size:11px;padding:4px 18px;margin-top:14px}
.course hr{border:0;border-top:1px solid #3d8bd0;margin:22px 0}
.post{width:345px;height:150px}
.post .ph{position:absolute;left:0;top:0;width:150px;height:150px}
.post .body{position:absolute;left:170px;top:0;white-space:nowrap}
.post h5{font-size:14px;font-weight:400;color:#222}
.post .meta{font-size:11px;font-style:italic;color:var(--orange);margin:10px 0 6px}
.post p{font-size:12px;line-height:18px;color:#444}
.post .more{font-size:14px;color:var(--orange);margin-top:10px}
.prof{width:216px;height:90px}
.prof .av{position:absolute;left:0;top:0;width:81px;height:81px;border-radius:50%;border:3px solid #fff;background:radial-gradient(circle,#9a8a7a 0%,#555 100%)}
.prof .body{position:absolute;left:100px;top:3px;width:116px;white-space:nowrap}
.prof h6{font-size:14px;font-weight:400;color:var(--orange)}
.prof p{font-size:12px;line-height:17px;color:#444}
.view-all{left:866px;top:1829px;width:187px;height:30px;border-radius:15px;background:var(--blue);color:#fff;font-size:14px;font-weight:600;text-align:center;line-height:30px}
.footer{left:0;top:1916px;width:1200px;height:383px;background:var(--footer);color:#ddd}
.footer h4{position:absolute;top:30px;font-size:18px;font-weight:400;color:#fff}
.footer .about p{font-size:12px;line-height:18px;color:#ddd;white-space:nowrap}
.fbrand{display:flex;align-items:center;gap:8px;margin:18px 0 8px}
.fbrand i{flex:0 0 34px;height:34px;border-radius:50%;background:#fff}
.fbrand b{font-weight:400;font-size:14px;line-height:17px;color:var(--orange)}
.gallery{display:grid;grid-template-columns:88px 88px;gap:6px}
.gallery span{height:81px;background:linear-gradient(135deg,#4a74c4,#2a4f9a)}
.why ul{list-style:none}
.why li{font-size:11px;height:29px;color:#bbb;white-space:nowrap}
.why li::before{content:"→ ";color:#ccc}
.why li.hot{color:var(--orange)}
.contact label{display:block;font-size:11px;font-weight:700;color:#ddd;margin-bottom:8px}
.contact .in{background:#fff;height:34px;border-radius:3px;margin-bottom:22px}
.contact .ta{height:75px}
.contact .submit{display:inline-block;background:var(--orange);color:#fff;font-size:14px;font-weight:700;padding:3px 14px;border-radius:2px;margin-top:-6px}
.bottom{left:0;top:2299px;width:1200px;height:42px;background:var(--footer-deep);color:#fff;font-size:12px}
.bottom span{position:absolute;top:13px}
</style>
</head>
<body>
<div class="abs topbar">
  <ul><li>About The Education System</li><li>About The Education System</li><li>Research</li></ul>
  <div class="social"><span></span><span></span><span></span><span></span><span></span></div>
</div>
<header class="abs header">
  <div class="brand"><i></i><b>Brightwave</b></div>
  <div class="search">Enter your keywords...
    <svg width="10" height="10" viewBox="0 0 10 10"><circle cx="4" cy="4" r="3" fill="none" stroke="#888" stroke-width="1.3"/><line x1="6.2" y1="6.2" x2="9" y2="9" stroke="#888" stroke-width="1.3"/></svg>
  </div>
</header>
<nav class="abs nav">
  <a class="active">Home 首页</a>
  <div class="items">
    <a>Lakeview Summer Program 暑期班</a>
    <a>Maple Grove Summer Camp 夏令营</a>
    <a>Whole Year Program 全年项目</a>
    <a>Harborview University 大学</a>
  </div>
</nav>
<div class="abs hero" role="img" aria-label="Photo of US and Chinese students sharing a meal at an outdoor café"></div>
<div class="abs hero-caption">
  <h1>BRIGHTWAVE</h1>
  <h2>Education Program Between US And China</h2>
  <p>Lorem Ipsum est simplement du faux texte employé dans la sition et la misen page avant impression...Lorem Ipsum est simplement du faux texte employé dans la sition et la misen page avant impression...</p>
  <span class="btn-read">READ MORE</span>
</div>
<div class="abs dots"><span></span><span></span><span></span><span></span></div>

<div class="abs perk" style="left:130px;top:687px">
  <svg width="50" height="40" viewBox="0 0 50 40"><path d="M3 12 L25 3 L47 12 L25 21 Z" fill="var(--blue)"/><path d="M12 17 v10 q13 7 26 0 v-10 l-13 6z" fill="var(--blue)"/><line x1="44" y1="13" x2="44" y2="30" stroke="var(--blue)" stroke-width="2"/></svg>
  <h3>Better Education</h3><p>Lorem Ipsum est simplement<br>du faux &nbsp;dans la sition et l<br>a misen page avant</p></div>
<div class="abs perk" style="left:362px;top:687px">
  <svg width="44" height="44" viewBox="0 0 44 44"><circle cx="20" cy="20" r="15" fill="none" stroke="var(--blue)" stroke-width="5"/><path d="M12 20 l6 6 l12 -12" fill="none" stroke="var(--blue)" stroke-width="4"/></svg>
  <h3>Quality Understanding</h3><p>Lorem Ipsum est simplement<br>du faux &nbsp;dans la sition et l<br>a misen page avant</p></div>
<div class="abs perk" style="left:621px;top:687px">
  <svg width="40" height="40" viewBox="0 0 40 40" stroke="var(--blue)" stroke-width="3"><line x1="20" y1="3" x2="20" y2="37"/><line x1="5" y1="11" x2="35" y2="29"/><line x1="5" y1="29" x2="35" y2="11"/></svg>
  <h3>Different Atmosphere</h3><p>Lorem Ipsum est simplement<br>du faux &nbsp;dans la sition et l<br>a misen page avant</p></div>
<div class="abs perk" style="left:874px;top:687px;width:200px">
  <svg width="40" height="44" viewBox="0 0 40 44"><circle cx="18" cy="16" r="12" fill="none" stroke="var(--blue)" stroke-width="3"/><path d="M6 28 q12 10 24 0" fill="none" stroke="var(--blue)" stroke-width="3"/><line x1="18" y1="32" x2="18" y2="40" stroke="var(--blue)" stroke-width="3"/></svg>
  <h3>Intensive Learning</h3><p>Lorem Ipsum est simplement<br>du faux &nbsp;dans la sition et l<br>a misen page avant impres-</p></div>

<div class="abs sec-title" style="left:130px;top:832px;width:940px">Our Features</div>
<div class="abs feature" style="left:130px;top:875px"><div class="ph" role="img" aria-label="Photo of students at a classroom table" style="background:linear-gradient(135deg,#8a7050,#c9a830)"></div><p>Lorem Ipsum est simplement du faux<br>exte mployé dans la ion et la misen<br>page avant impression...dans daster<br>a misen page avant impression...<br>simplement du faux exte mployé.......</p><span class="btn">Learn More</span></div>
<div class="abs feature" style="left:370px;top:875px"><div class="ph" role="img" aria-label="Photo of students playing a group game indoors" style="background:linear-gradient(135deg,#c8b8a0,#3a5ab0)"></div><p>Lorem Ipsum est simplement du faux<br>exte mployé dans la ion et la misen<br>page avant impression...dans daster<br>a misen page avant impression...<br>simplement du faux exte mployé.......</p><span class="btn">Learn More</span></div>
<div class="abs feature" style="left:610px;top:875px"><div class="ph" role="img" aria-label="Photo of students on a bike ride in a park" style="background:linear-gradient(180deg,#9ab0a8,#4a7a40)"></div><p>Lorem Ipsum est simplement du faux<br>exte mployé dans la ion et la misen<br>page avant impression...dans daster<br>a misen page avant impression...<br>simplement du faux exte mployé.......</p><span class="btn">Learn More</span></div>
<div class="abs feature" style="left:850px;top:875px"><div class="ph" role="img" aria-label="Group photo of program students" style="background:linear-gradient(135deg,#c04040,#d8b080)"></div><p>Lorem Ipsum est simplement du faux<br>exte mployé dans la ion et la misen<br>page avant impression...dans daster<br>a misen page avant impression...<br>simplement du faux exte mployé.......</p><span class="btn">Learn More</span></div>

<div class="abs sec-title" style="left:130px;top:1210px;width:590px">Interesting Videos of Students</div>
<div class="abs videos" style="left:130px;top:1244px;width:600px">
  <p>Lorem Ipsum est simplement du faux texte mployé dans la ion et la misen page avant impression...dans la ion et la misen page avant impression...Lorem Ipsum est simplement du faux texte mployé dans la ion et la misen pageavanimpression...dans la ion et la misen page avant impression...</p>
  <ul>
    <li><svg width="20" height="8"><path d="M0 4h16M12 0l5 4-5 4" fill="none" stroke="var(--blue)" stroke-width="2"/></svg>Simplement du faux texte employé dans la sition et la misen</li>
    <li class="hot"><svg width="20" height="8"><path d="M0 4h16M12 0l5 4-5 4" fill="none" stroke="var(--blue)" stroke-width="2"/></svg>Lorem Ipsum est simplement du faux</li>
    <li><svg width="20" height="8"><path d="M0 4h16M12 0l5 4-5 4" fill="none" stroke="var(--blue)" stroke-width="2"/></svg>Simplement du faux texte employé dans la sition et la misen</li>
  </ul>
</div>
<div class="abs player" role="img" aria-label="Video still of students lined up in a school hallway"></div>
<div class="abs player-bar">
  <svg width="319" height="30" viewBox="0 0 319 30"><rect x="14" y="10" width="3" height="10" fill="#fff"/><rect x="20" y="10" width="3" height="10" fill="#fff"/><text x="45" y="19" font-size="7" fill="#ccc" font-family="Open Sans,sans-serif">00:04:21 / 00:08:20</text><path d="M212 11v8M212 19a2 2 0 1 1-1-1" stroke="#fff" fill="none"/><rect x="225" y="14" width="36" height="2" fill="var(--orange)"/><path d="M298 9h5M298 9v5M308 21h-5M308 21v-5" stroke="#fff" fill="none"/></svg>
</div>

<div class="abs sec-title" style="left:130px;top:1470px;width:304px">Course Search</div>
<div class="abs course">
  <h4>Courses Of &nbsp;Sciences</h4>
  <div class="field">Keywords</div>
  <span class="btn">Read More</span>
  <hr>
  <h4>Courses Of Other Faculties</h4>
  <div class="field">Keywords</div>
  <span class="btn">Read More</span>
</div>

<div class="abs sec-title" style="left:470px;top:1470px;width:345px">Campus News</div>
<div class="abs post" style="left:470px;top:1521px">
  <div class="ph" role="img" aria-label="Photo of students with a plush toy at an indoor event" style="background:linear-gradient(135deg,#c8a060,#8a4a3a)"></div>
  <div class="body"><h5>A Sample Of Standard Post</h5><div class="meta">04 May 2013 | 12 Comments</div><p>Lorem Ipsum est simplement<br>du faux &nbsp;dans la sition et l<br>a misen page avant</p><div class="more">Read More &gt;&gt;</div></div>
</div>
<div class="abs post" style="left:470px;top:1712px">
  <div class="ph" role="img" aria-label="Photo of two students wrapped in their national flags" style="background:linear-gradient(135deg,#9ab0c0,#c03030 60%,#3a4a8a)"></div>
  <div class="body"><h5>A Sample Of Standard Post</h5><div class="meta">04 May 2013 | 12 Comments</div><p>Lorem Ipsum est simplement<br>du faux &nbsp;dans la sition et l<br>a misen page avant</p><div class="more">Read More &gt;&gt;</div></div>
</div>

<div class="abs sec-title" style="left:854px;top:1470px;width:216px">Professors</div>
<div class="abs prof" style="left:854px;top:1517px"><div class="av" role="img" aria-label="Portrait of professor"></div><div class="body"><h6>Henry Dalton</h6><p>Lorem Ipsum est<br>simplement du faux<br>dans .....</p></div></div>
<div class="abs prof" style="left:854px;top:1620px"><div class="av" role="img" aria-label="Portrait of professor"></div><div class="body"><h6>James Orwin</h6><p>Lorem Ipsum est<br>simplement du faux<br>dans .....</p></div></div>
<div class="abs prof" style="left:854px;top:1720px"><div class="av" role="img" aria-label="Portrait of professor"></div><div class="body"><h6>Carles Brandt</h6><p>Lorem Ipsum est simple-<br>ment du faux dans ....<br>a sition et l</p></div></div>
<div class="abs view-all">View All</div>

<footer class="abs footer">
  <h4 style="left:137px">About US</h4>
  <div class="abs about" style="left:130px;top:64px;width:210px">
    <div class="fbrand"><i></i><b>Brightwave Youth<br>Academy</b></div>
    <p>Lorem Ipsum est simplement du faux<br>exte mployé dans la ion et la misen<br>page avant impression...dans daster<br>a misen page avant impression...<br>simplement du faux exte mployé dans<br>la ion et la misen page avant<br>Lorem Ipsum est simplement du faux<br>exte mployé dans la ion et la misen<br>page avant impression...dans daster<br>a misen page avant impression...</p>
  </div>
  <h4 style="left:375px">Gallery</h4>
  <div class="abs gallery" style="left:374px;top:72px" role="img" aria-label="Thumbnail grid of student photos in blue tint"><span></span><span></span><span></span><span></span><span></span><span></span></div>
  <h4 style="left:607px">Why Choose US</h4>
  <div class="abs why" style="left:607px;top:68px"><ul>
    <li class="hot">Lorem Ipsum est simplement</li><li>Suspendisse id justo non liber</li><li>Lorem Ipsum est simplement</li><li>Suspendisse id justo non liber</li><li>Suspendisse id justo non liber</li><li>Lorem Ipsum est simplement</li><li>Suspendisse id justo non liber</li><li>Lorem Ipsum est simplement</li>
  </ul></div>
  <h4 style="left:832px">Contact US</h4>
  <div class="abs contact" style="left:832px;top:68px;width:231px">
    <label>Name</label><div class="in"></div>
    <label>Email</label><div class="in"></div>
    <label>Message</label><div class="in ta"></div>
    <span class="submit">Submit</span>
  </div>
</footer>
<div class="abs bottom">
  <span style="left:131px">Copyright © 2013 Brightwave ltd All Rights Reserved</span>
  <span style="left:838px">Terms &amp; Condition</span>
  <span style="left:966px">|</span>
  <span style="left:996px">Privacy Policy</span>
</div>
</body>
</html>
```